Veridane Works, Inc. - Update our Website

Veridane Works needs a website to help our customers to navigate through our services efficiently. Our existing website is at www.verowk.example

We would like to explain our services with content and pictures (photographs) that distinguishes our products and services from our competition.

The website design must implement a strategy to focus on our Contract Labeling services.

With this new design we would like to attract new customers and ensure that our existing customers are fully informed with our latest offerings.

```html
<!DOCTYPE html>
<html lang="en">
<head>
<meta charset="utf-8">
<title>Veridane Works, Inc.</title>
<link href="https://fonts.googleapis.com/css2?family=Arimo:wght@400;700&display=swap" rel="stylesheet">
<style>
:root{
  --blue:#2f90c8;
  --green:#86c426;
  --orange:#f68b28;
  --text:#666;
  --heading:#555;
  --light:#f6f4f4;
  --card:#fff;
  --footer:#2b2b2b;
  --footer-panel:#3b3b3b;
  --footer-bar:#262626;
  --footer-text:#b9b9b9;
  --field:#4a4a4a;
}
*{margin:0;padding:0;box-sizing:border-box}
html,body{width:1200px;height:1129px;overflow:hidden}
body{font-family:"Arimo",Arial,sans-serif;color:var(--text);background:#fff;position:relative}
.wrap{position:absolute;left:299px;width:586px}

.site-header{position:absolute;top:0;left:0;width:1200px;height:52px;background:#fff}
.brand{position:absolute;left:299px;top:12px;display:flex;align-items:center;gap:9px}
.brand-dot{width:30px;height:30px;border-radius:50%;background:var(--green)}
.brand-name{font-size:17px;font-weight:700;color:#222;letter-spacing:.5px}
.main-nav{position:absolute;right:315px;top:22px;display:flex;gap:19px;font-size:8.5px;color:#444;letter-spacing:.2px}

.hero{position:absolute;top:52px;left:0;width:1200px;height:302px;
  background:linear-gradient(100deg,#dfe6ea 0%,#5c6b73 25%,#2c3338 45%,#6f7d86 62%,#c7d4db 78%,#8fb7c6 90%,#d97a8a 100%)}

.highlights{top:326px;height:94px;display:flex}
.highlight{width:195.33px;background:var(--light)}
.highlight h3{height:28px;color:#fff;font-size:10.5px;font-weight:700;padding:8px 11px 0}
.highlight p{font-size:8.5px;line-height:11px;padding:11px 11px 0;color:#777}
.highlight a{display:block;font-size:6px;font-weight:700;padding:7px 11px;text-decoration:none}
.hl-blue h3{background:var(--blue)} .hl-blue a{color:var(--blue)}
.hl-green h3{background:var(--green)} .hl-green a{color:var(--green)}
.hl-orange h3{background:var(--orange)} .hl-orange a{color:var(--orange)}
.hl-green{background:#f1f0f0}

.welcome{top:455px;text-align:center}
.welcome h1{font-size:14.5px;font-weight:400;color:var(--heading)}
.welcome p{margin:21px auto 0;width:460px;font-size:8.5px;line-height:11.5px;color:#888}

.services-band{position:absolute;top:546px;left:0;width:1200px;height:278px;background:var(--light)}
.services-band .notch{position:absolute;left:584px;top:0;width:0;height:0;border-left:9px solid transparent;border-right:9px solid transparent;border-top:9px solid #fff}
.services-band h2{position:absolute;top:31px;width:1200px;text-align:center;font-size:14.5px;font-weight:400;color:var(--heading)}
.cards{top:610px;display:flex;gap:14px}
.card{width:186px;height:178px;background:var(--card)}
.card-photo{height:101px}
.card h4{font-size:10px;color:#555;padding:16px 11px 0}
.card p{font-size:7.5px;line-height:10.5px;color:#888;padding:8px 11px 0}
.card p b{color:#555}
.ph1{background:linear-gradient(135deg,#cfe5f0,#5aa6c8 50%,#e6edf1)}
.ph2{background:linear-gradient(135deg,#dcdcdc,#7a7a7a 55%,#bdbdbd)}
.ph3{background:linear-gradient(135deg,#1e1e1e,#6e6e6e 50%,#d9d9d9)}

.site-footer{position:absolute;top:824px;left:0;width:1200px;height:267px;background:var(--footer)}
.foot-brand{position:absolute;left:301px;top:32px;display:flex;align-items:center;gap:7px}
.foot-brand .brand-dot{width:22px;height:22px;background:#999}
.foot-brand .brand-name{font-size:12px;color:#ddd}
.address{position:absolute;left:329px;font-size:7.5px;line-height:11px;color:var(--footer-text)}
.address .gap{height:9px}
.site-links{position:absolute;left:498px;top:36px;width:170px}
.site-links h5,.contact-form h5{font-size:8px;font-weight:700;color:#ddd;letter-spacing:.3px}
.site-links hr{border:0;border-top:1px solid #777;margin:8px 0 10px}
.link-cols{display:flex}
.link-cols ul{list-style:none;width:94px;font-size:7.5px;line-height:17.7px;color:var(--footer-text);padding-left:2px}
.contact-form{position:absolute;left:720px;top:0;width:165px;height:267px;background:var(--footer-panel);padding:40px 15px 0}
.field{margin-top:9px;height:24px;border:1px solid #777;background:var(--field);font-size:7px;color:#999;padding:7px 7px 0}
.contact-form h5+.field{margin-top:10px}
.field.area{height:65px}
.submit{margin-top:11px;width:65px;height:25px;background:var(--blue);color:#fff;font-size:9px;font-weight:700;text-align:center;line-height:25px;border:0}

.footer-bar{position:absolute;top:1091px;left:0;width:1200px;height:38px;background:var(--footer-bar);border-top:1px solid #3a3a3a}
.copyright{position:absolute;left:299px;top:14px;font-size:7px;color:#888}
.social{position:absolute;left:811px;top:14px;display:flex;gap:5px}
.social span{width:15px;height:15px}
</style>
</head>
<body>
<header class="site-header">
  <div class="brand"><span class="brand-dot"></span><span class="brand-name">VERIDANE WORKS, INC.</span></div>
  <nav class="main-nav"><span>HOME</span><span>ABOUT US</span><span>SERVICES</span><span>USER SUPPORT</span><span>CONTACT US</span></nav>
</header>

<div class="hero" role="img" aria-label="Laboratory scene with a microscope, a molecule model and glass flasks"></div>

<section class="wrap highlights">
  <div class="highlight hl-blue"><h3>VeriPro/LBL™</h3><p>VeriPro/LBL™ is the industry's leading clini-cal label generation system offering...</p><a>READ MORE</a></div>
  <div class="highlight hl-green"><h3>Software Validation Services</h3><p>Veridane Works offers software validation services for the FDA regulated...</p><a>READ MORE</a></div>
  <div class="highlight hl-orange"><h3>VeriStock™</h3><p>VeriStock™ is a premium line of label prod-ucts that we supply...</p><a>READ MORE</a></div>
</section>

<section class="wrap welcome">
  <h1>Welcome to Veridane Works Inc.</h1>
  <p>Veridane Works, Inc. specializes in providing products and services to the pharmaceutical industry. We are focused on the needs of those individuals involved with Clinical Trial Materials.</p>
</section>

<section class="services-band">
  <span class="notch"></span>
  <h2>Our Services</h2>
</section>
<div class="wrap cards">
  <article class="card"><div class="card-photo ph1" role="img" aria-label="Scientist working at a microscope"></div><h4>VeriServ™</h4><p>VeriServ™ is a contract clinical label generation service that provides you with ready to apply clinical labels specifically... <b>read more</b></p></article>
  <article class="card"><div class="card-photo ph2" role="img" aria-label="Rows of laboratory glassware"></div><h4>VeriBook™</h4><p>VeriBook™ labels are multi-page clinical labels used to address the needs of multi-language studies... <b>read more</b></p></article>
  <article class="card"><div class="card-photo ph3" role="img" aria-label="Clinician reviewing data at a workstation"></div><h4>Clinical Randomizations</h4><p>Our systems can create randomization data for all types of CTM requirements... <b>read more</b></p></article>
</div>

<footer class="site-footer">
  <div class="foot-brand"><span class="brand-dot"></span><span class="brand-name">VERIDANE WORKS, INC.</span></div>
  <div class="address" style="top:66px">412 ALDER LANE<br>MILLBROOK<br>NY 11500-0412 USA<div class="gap"></div>PHONE: &nbsp;&nbsp;&nbsp;&nbsp;&nbsp;+1-555-014-6200<br>FAX: &nbsp;&nbsp;+1-555-014-2620</div>
  <div class="address" style="top:154px">88 HARROW STREET<br>EASTFIELD<br>NJ 08500 USA<div class="gap"></div>PHONE: +1-555-019-0040<br>FAX: +1-555-019-8266</div>
  <div class="site-links">
    <h5>SITE LINK</h5><hr>
    <div class="link-cols">
      <ul><li>Home</li><li>About Us</li><li>Services</li><li>User Support</li><li>Contact Us</li></ul>
      <ul><li>VeriServ</li><li>VeriBook</li><li>Randomizations</li><li>VeriPro/LBL</li><li>Validation</li><li>VeriStock</li></ul>
    </div>
  </div>
  <div class="contact-form">
    <h5>CONTACT FORM</h5>
    <div class="field">Name</div>
    <div class="field">E-mail</div>
    <div class="field">Telephone</div>
    <div class="field area">Comments</div>
    <div class="submit">SUBMIT</div>
  </div>
</footer>
<div class="footer-bar">
  <span class="copyright">Copyright © 2014 Veridane Works, Inc.</span>
  <div class="social"><span style="background:#3b5998"></span><span style="background:#2aa3df"></span><span style="background:#555"></span><span style="background:#f68b28"></span></div>
</div>
</body>
</html>
```